Design the Business card for NetVaultix

Business card required for a professional Cyber Security business.
Company Logo and Icon has already been provided however I would like other options for the logo and icon to compare to. Alternatively, please refine/enhance the image of the logo.icon I have already provided.

If you are going to use the provided logo and icon, I was thinking that the company raised Logo on White background would serve well on the front of the card. See attached. AND, a large company raised stand-alone icon to appear on black background on the back of the card with tagline 'Cyber Risk Management, Governance and Consulting' or 'Cyber Security for your Business' See attached.
Alternatively, provide your own design for the logo and icon.

Target Market(s)

Enterprise, Government, Financial.

Contact Information for Business Card

Teodor Vaskelin
Founder and CEO

Email Address
Mobile Number
Website URL
LinkedIn URL

Logo Text

NetVaultix - see attached example of logo

Font styles to use
Other font styles liked:
• Berlin Sans FB

Requirements
Must have
• Clean large and bold icon on the back with tagline.
• Horizontal alignment,
Nice to have
• Round edges.
• Raised Logo/Icon
Should not have
• An unprofessional look and feel.

```html
<!DOCTYPE html>
<html lang="en">
<head>
<meta charset="utf-8">
<title>NetVaultix Business Card</title>
<link rel="stylesheet" href="https://fonts.googleapis.com/css2?family=Fredoka:wght@400;500&family=Roboto:wght@400&display=swap">
<style>
  :root {
    --page-bg: #2a2a2c;
    --card-blue: #0a6fc2;
    --card-white: #f6f7f8;
    --card-black: #1a1b1d;
    --brand-blue: #0b6fc0;
    --accent-yellow: #f5b800;
    --tag-blue: #4a78c8;
    --text-white: #ffffff;
  }
  html, body {
    margin: 0;
    width: 1200px;
    height: 960px;
    overflow: hidden;
    background: var(--page-bg);
  }
  .canvas { position: relative; width: 1200px; height: 960px; }
  .card {
    position: absolute;
    width: 600px;
    height: 342px;
    overflow: hidden;
    box-shadow: 0 4px 10px rgba(0,0,0,0.5);
  }
  .card-front { left: 314px; top: 113px; background: var(--card-blue); }
  .card-back { left: 311px; top: 472px; background: var(--card-black); }
  .front-panel { position: absolute; left: 0; top: 0; }
  .front-wordmark {
    position: absolute;
    left: 64px; top: 148px;
    font-family: "Fredoka", sans-serif;
    font-weight: 500;
    font-size: 40px;
    color: var(--brand-blue);
    margin: 0;
    line-height: 1;
  }
  .contact { position: absolute; left: 384px; top: 104px; color: var(--text-white); }
  .contact-name {
    font-family: "Fredoka", sans-serif;
    font-weight: 400;
    font-size: 21px;
    color: var(--accent-yellow);
    margin: 0; line-height: 1.1;
  }
  .contact-title {
    font-family: "Fredoka", sans-serif;
    font-size: 14px;
    margin: 2px 0 20px;
  }
  .contact-list { list-style: none; margin: 0; padding: 0; font-family: "Roboto", sans-serif; font-size: 14px; }
  .contact-list li { display: flex; align-items: center; height: 19px; }
  .contact-list svg { width: 14px; height: 14px; margin-right: 10px; flex: none; }
  .back-brand {
    position: absolute; left: 124px; top: 134px;
    display: flex; align-items: center;
  }
  .back-brand-dot { width: 68px; height: 68px; border-radius: 50%; background: var(--brand-blue); margin-right: 18px; }
  .back-wordmark {
    font-family: "Fredoka", sans-serif;
    font-weight: 500;
    font-size: 46px;
    color: var(--brand-blue);
    margin: 0;
  }
  .tagline {
    position: absolute; left: 0; right: 0; top: 276px;
    text-align: center;
    font-family: "Fredoka", sans-serif;
    font-size: 18px;
    color: var(--tag-blue);
    margin: 0;
  }
  .tagline-accent { color: var(--accent-yellow); }
</style>
</head>
<body>
<main class="canvas">
  <section class="card card-front">
    <svg class="front-panel" width="600" height="342" viewBox="0 0 600 342">
      <path d="M0 0 H268 C330 0 342 90 342 171 C342 252 330 342 262 342 H0 Z" fill="var(--card-white)"/>
    </svg>
    <p class="front-wordmark">NetVaultix</p>
    <div class="contact">
      <h1 class="contact-name">Teodor Vaskelin</h1>
      <p class="contact-title">Founder &amp; CEO</p>
      <ul class="contact-list">
        <li><svg viewBox="0 0 14 14"><rect x="3" y="0.5" width="8" height="13" rx="1.5" fill="none" stroke="var(--accent-yellow)" stroke-width="1.6"/><rect x="5.5" y="10.5" width="3" height="1.2" fill="var(--accent-yellow)"/></svg>555 014 2290</li>
        <li><svg viewBox="0 0 14 14"><rect x="0.5" y="3" width="13" height="9" fill="var(--accent-yellow)"/><path d="M0.5 3 L7 8 L13.5 3" fill="none" stroke="var(--card-blue)" stroke-width="1.2"/></svg>teodor@netvaultix.com</li>
        <li><svg viewBox="0 0 14 14"><circle cx="7" cy="7" r="6.5" fill="var(--accent-yellow)"/><path d="M0.5 7 H13.5 M7 0.5 C3.5 4 3.5 10 7 13.5 M7 0.5 C10.5 4 10.5 10 7 13.5" fill="none" stroke="var(--card-blue)" stroke-width="1"/></svg>www.netvaultix.com</li>
        <li><svg viewBox="0 0 14 14"><circle cx="7" cy="7" r="6.5" fill="var(--accent-yellow)"/></svg>netvaultix</li>
      </ul>
    </div>
  </section>

  <section class="card card-back">
    <div class="back-brand">
      <span class="back-brand-dot"></span>
      <p class="back-wordmark">NetVaultix</p>
    </div>
    <p class="tagline">Cyber Risk Management, <span class="tagline-accent">Governance &amp; Consulting</span></p>
  </section>
</main>
</body>
</html>
```